Frischer, moderner, emotionaler Baumarkt-Onlineshop sucht passende Außendarstellung
Zielgruppe
Wir sind gerade im Aufbau eines Onlinebaumarktes. In diesem Baumarkt bekommt man vom Nagel bis hin zum neuen Fußboden alles was das Herz begehrt. Wir möchten der Begleiter für jeden Heimwerker sein, der eine gute Beratung, hochwertige Produkte und einen aufgeräumten Fachhandel sucht. Wir wollen einen emotionalen Onlineshop schaffen, bei dem das richtige Produkt dich sucht und nicht du stundenlang das richtige Produkt.
Aufgabenstellung
Wir möchten ein modernes und frisches Bild, der etwas eingestaubten Baumarktlandschaft vermitteln. Bei uns soll es Spaß machen, nach tollen Produkten zu stöbern. Der Kunde soll visuell angesprochen werden und sich intuitiv auf unseren Seiten bewegen können. Wenn man sich die gängigen Shopseiten anschaut, hat man eine ewig lange Navigation um zu seinem Produkt zu kommen. Wir möchten diesen Prozess, durch intelligente Filter gerne verkürzen, so dass jeder Laie sein Produkt ganz leicht findet.
Die Farben der Seite sollten sich an das Logo anlehnen oder diese auch einfließen lassen, damit die Seite wie aus einem Guss wirkt. Interessieren würde uns auch wie die Seite nicht nur auf dem Desktop aussieht, sondern auch seine Übersichtigkeit auf einem Tablet oder Smartphone beibehält.

```html
<!DOCTYPE html>
<html lang="de">
<head>
<meta charset="utf-8">
<title>werkstolz-markt.de – Böden</title>
<link href="https://fonts.googleapis.com/css2?family=Roboto+Condensed:wght@400;700&display=swap" rel="stylesheet">
<style>
:root{
  --blue:#1d3d8f;
  --green:#84b817;
  --grey:#efefef;
  --text:#444;
  --line:#ccc;
}
*{margin:0;padding:0;box-sizing:border-box}
html,body{width:1200px;height:2784px;overflow:hidden;background:#fff}
body{position:relative;font-family:"Roboto Condensed",sans-serif;color:var(--text);font-size:12px}
.abs{position:absolute}
.header{left:0;top:0;width:1200px;height:98px}
.logo{left:126px;top:34px;font-size:28px;font-weight:700;color:var(--blue);line-height:1}
.logo small{display:block;font-size:14px;text-align:right}
.nav{left:303px;top:54px;display:flex;gap:19px;font-weight:700;font-size:13px;color:var(--blue);letter-spacing:.3px}
.search{left:699px;top:54px}
.account{left:930px;top:56px;font-size:11px;color:#555}
.cart{left:1010px;top:50px;display:flex;align-items:center;gap:4px;color:var(--green);font-size:11px;font-weight:700}
.hero{left:0;top:98px;width:1200px;height:153px;background:linear-gradient(100deg,#d9b98a,#edd6b1 45%,#f7ead4 70%,#dcbb8c)}
.hero h1{position:absolute;left:154px;top:96px;color:#fff;font-size:36px;font-weight:700}
.crumb{left:155px;top:261px;font-size:11px;color:#333}
.intro{left:125px;top:283px;width:648px;height:280px;background:var(--grey);padding:40px 29px}
.intro h2{font-size:23px;color:#222;font-weight:700;margin-bottom:20px}
.intro p{font-size:11.5px;line-height:16.5px;width:500px;margin-bottom:16px}
.video{left:704px;top:298px;width:371px;height:243px;background:linear-gradient(90deg,#e8e8e6,#f4f4f2 50%,#9c6a3f)}
.play{left:877px;top:394px}
.brands{left:218px;top:596px;display:flex;gap:21px}
.brands span{display:block;width:110px;height:36px;background:#ddd}
.photo-lam{left:71px;top:674px;width:529px;height:283px;background:linear-gradient(180deg,#c6d0d0 0%,#d6dcdb 55%,#6e6a66 70%,#5b5753)}
.photo-par{left:599px;top:1022px;width:530px;height:305px;background:linear-gradient(180deg,#e9e3d8 0%,#d9cfbf 55%,#a89b88 80%,#b7ad9c)}
.feature h3{font-size:23px;color:var(--blue);font-weight:700;margin-bottom:18px}
.feature p{font-size:11.5px;line-height:16.7px;width:340px}
.btn{position:absolute;height:27px;border-radius:14px;background:var(--blue);color:#fff;font-weight:700;font-size:11.5px;display:flex;align-items:center;justify-content:center}
.section-title{left:0;width:1200px;top:1380px;text-align:center;font-size:20px;font-weight:700;color:var(--blue)}
.prod{position:absolute;width:200px;text-align:center}
.prod .img{width:135px;height:128px;margin:0 auto 16px}
.prod b{display:block;font-size:11.5px;color:var(--blue);margin-bottom:6px}
.prod i{font-style:normal;font-weight:700;font-size:13px;color:var(--green)}
.wood1{background:linear-gradient(90deg,#d6d6d6,#c2c2c2 25%,#dadada 50%,#bdbdbd 75%,#d3d3d3)}
.wood2{background:radial-gradient(circle at 50% 55%,#6c5238,#8a6a48 60%,#9b7c59)}
.wood3{background:linear-gradient(180deg,#c59659,#b9884f 50%,#c79c62)}
.filterbar{left:125px;top:1666px;width:950px;height:37px;background:var(--green);color:#fff;font-weight:700;font-size:11.5px}
.filterbar .f{position:absolute;left:14px;top:10px;display:flex;gap:8px;align-items:center}
.filterbar .s{position:absolute;right:14px;top:6px;display:flex;gap:10px;align-items:center}
.sel{display:flex;justify-content:space-between;align-items:center;border:1px solid var(--line);background:#fff;height:24px;padding:0 8px;font-weight:400;color:#555;font-size:11px}
.filters{left:147px;top:1721px;display:flex;gap:34px;align-items:center;font-size:11.5px;font-weight:700;color:#333}
.filters label{display:flex;gap:8px;align-items:center}
.footer-logo{left:240px;top:2555px;font-size:18px;font-weight:700;color:var(--blue);line-height:1}
.footer-logo small{display:block;font-size:8px;text-align:right}
.fcol{top:2524px;font-size:10.5px;color:var(--blue);line-height:15px}
.fcol h4{font-size:12px;margin-bottom:12px}
.phone{font-size:16px;margin-top:12px}
.legal{left:0;width:1200px;text-align:center;font-size:9px;color:#444}
</style>
</head>
<body>
<header class="abs header">
  <div class="abs logo">werkstolz<small>-markt.de</small></div>
  <nav class="abs nav"><span>BÖDEN</span><span>TÜREN</span><span>GARTEN</span><span>WAND &amp; DECKE</span><span>BAUEN MIT HOLZ</span></nav>
  <svg class="abs search" width="14" height="14" viewBox="0 0 14 14"><circle cx="6" cy="6" r="4.5" fill="none" stroke="#1d3d8f" stroke-width="1.5"/><path d="M9.5 9.5 13 13" stroke="#1d3d8f" stroke-width="1.5"/></svg>
  <div class="abs account">Mein Konto</div>
  <div class="abs cart"><svg width="18" height="16" viewBox="0 0 18 16"><path d="M1 2h3l2 8h9l2-6H5" fill="none" stroke="#333" stroke-width="1.4"/><circle cx="7" cy="13" r="1.4" fill="#333"/><circle cx="14" cy="13" r="1.4" fill="#333"/></svg>49,95 € *</div>
</header>
<section class="abs hero" role="img" aria-label="Heller Holzdielenboden im Sonnenlicht"><h1>Böden</h1></section>
<div class="abs crumb">Startseite &gt; Böden</div>
<section class="abs intro">
  <h2>Traumhafte Böden für Häuser und Wohnungen</h2>
  <p>Fast 500 verschiedene Böden stellen wir hier aus, damit Sie sich einen ersten Eindruck machen können. 50 Bodenmuster sind sogar original verlegt und beschreitbar - so können Sie nicht nur sehen, wie Ihre neuen Böden wirken, sondern auch fühlen, wie es sich auf ihnen läuft. Unsere Fachberater stehen Ihnen bei der Wahl mit ihrem Wissen zur Seite und können Ihnen zu allen Böden praktische Informationen geben, etwa zur Verlegung, der Oberflächenbehandlung oder der späteren Pflege und Reinigung.</p>
  <p>Gerne klären wir im gemeinsamen Gespräch, welche Böden Ihren Ansprüche an Optik, Robustheit und Laufgefühl entsprechen. Und damit später alles passt, besuchen wir Sie auf Wunsch auch zu Hause in Neumünster, Hamburg oder Kiel, um ein genaues Aufmaß zu nehmen.</p>
</section>
<div class="abs video" role="img" aria-label="Video: Beraterin in einem hellen Raum mit Holzboden"></div>
<svg class="abs play" width="44" height="44" viewBox="0 0 44 44"><circle cx="22" cy="22" r="22" fill="#333" opacity=".75"/><path d="M17 12 32 22 17 32z" fill="#fff"/></svg>
<div class="abs brands"><span></span><span></span><span></span><span></span><span></span><span></span></div>

<div class="abs photo-lam" role="img" aria-label="Wohnraum mit grauem Laminatboden und weißem Sessel"></div>
<div class="abs feature" style="left:691px;top:722px">
  <h3>Laminat</h3>
  <p>Sed ut perspiciatis unde omnis iste natus error sit voluptatem accusantium doloremque laudantium, totam rem aperiam, eaque ipsa quae ab illo inventore veritatis et quasi architecto beatae vitae dicta sunt explicabo. Nemo enim ipsam voluptatem quia voluptas sit aspernatur aut odit aut fugit, sed quia consequuntur magni dolores eos qui ratione voluptatem sequi nesciunt. Neque porro quisquam est, qui dolorem ipsum quia dolor sit amet, consectetur, adipisci velit.</p>
</div>
<div class="btn" style="left:788px;top:908px;width:142px">Laminatböden ansehen</div>

<div class="abs feature" style="left:206px;top:1064px">
  <h3>Parkett</h3>
  <p>Sed ut perspiciatis unde omnis iste natus error sit voluptatem accusantium doloremque laudantium, totam rem aperiam, eaque ipsa quae ab illo inventore veritatis et quasi architecto beatae vitae dicta sunt explicabo. Nemo enim ipsam voluptatem quia voluptas sit aspernatur aut odit aut fugit, sed quia consequuntur magni dolores eos qui ratione voluptatem sequi nesciunt. Neque porro quisquam est, qui dolorem ipsum quia dolor sit amet, consectetur, adipisci velit.</p>
</div>
<div class="btn" style="left:301px;top:1248px;width:143px">Parkettböden ansehen</div>
<div class="abs photo-par" role="img" aria-label="Helle Küche mit Esstisch und Parkettboden"></div>

<h2 class="abs section-title">Topseller der Kategorie Böden</h2>
<svg class="abs" style="left:124px;top:1495px" width="16" height="12" viewBox="0 0 16 12"><path d="M15 6H2M7 1 2 6l5 5" fill="none" stroke="#bbb" stroke-width="1.3"/></svg>
<svg class="abs" style="left:1060px;top:1495px" width="16" height="12" viewBox="0 0 16 12"><path d="M1 6h13M9 1l5 5-5 5" fill="none" stroke="#1d3d8f" stroke-width="1.3"/></svg>
<div class="prod" style="left:138px;top:1435px"><div class="img wood1" role="img" aria-label="Graue Holzoptik"></div><b>Hofwerk Sichtschutz Fjellby</b><i>85,99 €/St.*</i></div>
<div class="prod" style="left:377px;top:1435px"><div class="img wood2" role="img" aria-label="Dunkle Holzmaserung"></div><b>Gleitform Gleittür Weiß Lumo 3.1</b><i>1046,39 €/St.*</i></div>
<div class="prod" style="left:620px;top:1435px"><div class="img wood3" role="img" aria-label="Wildeiche Holzplatte"></div><b>Leimholzplatte Wildeiche (18 mm)</b><i>64,99 €/qm*</i></div>
<div class="prod" style="left:864px;top:1435px"><div class="img wood2" role="img" aria-label="Dunkle Holzmaserung"></div><b>Treppe Modell Stufara</b><i>14,99 €/qm*</i></div>

<div class="abs filterbar">
  <div class="f"><svg width="16" height="14" viewBox="0 0 16 14"><path d="M1 1h14L9.5 7v6l-3-1.5V7z" fill="none" stroke="#fff" stroke-width="1.5"/></svg>Filtern <span style="margin-left:12px">▼</span></div>
  <div class="s">Sortierung nach: <div class="sel" style="width:132px">Erscheinungsdatum <span>▼</span></div></div>
</div>
<div class="abs filters">
  <label>Art: <div class="sel" style="width:106px">Erle <span>▼</span></div></label>
  <label>Material: <div class="sel" style="width:106px">Laminatböden <span>▼</span></div></label>
  <label>Farbe: <div class="sel" style="width:120px">Hellbraun <span>▼</span></div></label>
  <label>Marke: <div class="sel" style="width:120px">Dielwerk <span>▼</span></div></label>
  <label>Maß: <div class="sel" style="width:120px">bis 500 g <span>▼</span></div></label>
</div>

<div class="prod" style="left:134px;top:1790px"><div class="img wood1" role="img" aria-label="Graue Holzoptik"></div><b>Hofwerk Sichtschutz Fjellby</b><i>85,99 €/St.*</i></div>
<div class="prod" style="left:374px;top:1790px"><div class="img wood2" role="img" aria-label="Dunkle Holzmaserung"></div><b>Gleitform Gleittür Weiß Lumo 3.1</b><i>1046,39 €/St.*</i></div>
<div class="prod" style="left:617px;top:1790px"><div class="img wood3" role="img" aria-label="Wildeiche Holzplatte"></div><b>Leimholzplatte Wildeiche (18 mm)</b><i>64,99 €/qm*</i></div>
<div class="prod" style="left:861px;top:1790px"><div class="img wood2" role="img" aria-label="Dunkle Holzmaserung"></div><b>Treppe Modell Stufara</b><i>14,99 €/qm*</i></div>

<div class="prod" style="left:134px;top:1997px"><div class="img wood1" role="img" aria-label="Graue Holzoptik"></div><b>Hofwerk Sichtschutz Fjellby</b><i>85,99 €/St.*</i></div>
<div class="prod" style="left:374px;top:1997px"><div class="img wood2" role="img" aria-label="Dunkle Holzmaserung"></div><b>Gleitform Gleittür Weiß Lumo 3.1</b><i>1046,39 €/St.*</i></div>
<div class="prod" style="left:617px;top:1997px"><div class="img wood3" role="img" aria-label="Wildeiche Holzplatte"></div><b>Leimholzplatte Wildeiche (18 mm)</b><i>64,99 €/qm*</i></div>
<div class="prod" style="left:861px;top:1997px"><div class="img wood2" role="img" aria-label="Dunkle Holzmaserung"></div><b>Treppe Modell Stufara</b><i>14,99 €/qm*</i></div>

<div class="prod" style="left:134px;top:2213px"><div class="img wood1" role="img" aria-label="Graue Holzoptik"></div><b>Hofwerk Sichtschutz Fjellby</b><i>85,99 €/St.*</i></div>
<div class="prod" style="left:374px;top:2213px"><div class="img wood2" role="img" aria-label="Dunkle Holzmaserung"></div><b>Gleitform Gleittür Weiß Lumo 3.1</b><i>1046,39 €/St.*</i></div>
<div class="prod" style="left:617px;top:2213px"><div class="img wood3" role="img" aria-label="Wildeiche Holzplatte"></div><b>Leimholzplatte Wildeiche (18 mm)</b><i>64,99 €/qm*</i></div>
<div class="prod" style="left:861px;top:2213px"><div class="img wood2" role="img" aria-label="Dunkle Holzmaserung"></div><b>Treppe Modell Stufara</b><i>14,99 €/qm*</i></div>

<div class="btn" style="left:529px;top:2444px;width:143px">mehr anzeigen</div>

<footer>
  <div class="abs footer-logo">werkstolz<small>-markt.de</small></div>
  <div class="abs fcol" style="left:397px">
    <h4>Service Hotline</h4>
    Telefonische Unterstützung und Beratung<br>unter:
    <div class="phone">40 - 987 654 321</div>
    Mo-Fr, 09:00 - 17:00 Uhr
  </div>
  <div class="abs fcol" style="left:639px">
    <h4>Shop Service</h4>
    Defektes Produkt<br>Partnerprogramm<br>rechtliche Vorabinformationen<br>Kontakt<br>Versand und Zahlungsbedingungen<br>Rückgabe<br>Widerrufsrecht<br>Widerrufsformular<br>AGB
  </div>
  <div class="abs fcol" style="left:881px">
    <h4>Informationen</h4>
    Newsletter<br>Über uns<br>Datenschutz<br>Impressum
  </div>
  <p class="abs legal" style="top:2726px">* Alle Preise inkl. gesetzl. Mehrwertsteuer zzgl. <span style="color:var(--blue);text-decoration:underline">Versandkosten</span> und ggf. Nachnahmegebühren, wenn nicht anders beschrieben.</p>
  <p class="abs legal" style="top:2747px">© 2017 werkstolz-markt.de. Alle Rechte vorbehalten.</p>
</footer>
</body>
</html>
```